Word template for proposals we send to clients

We want a word template designed based on the look/feel of our website. The website is www.brovexa.com.au and while we have pictures of 2 staff on the website we have pictures of other staff if required

the template will be used to send out proposals to potential clients, therefore it has to be professional, modern and compelling for someone to open

Target Market(s)

B2B

Industry/Entity Type

It Company

Font styles to use
Serif

Colors

Designer to choose colors to be used in the design.

Requirements
Must have
• Same look and feel as website
Nice to have
• Dont know what I am missing so anythign you feel i need to add

```html
<!DOCTYPE html>
<html lang="en">
<head>
<meta charset="utf-8">
<title>Brovexa – Proposal Word Template</title>
<link rel="stylesheet" href="https://fonts.googleapis.com/css2?family=Montserrat:wght@400;500;600;700;800&family=Open+Sans:wght@400;600;700&family=Roboto+Condensed:wght@400;700&display=swap">
<style>
  :root{
    --board:#e4e5e6;
    --navy:#1d3557;
    --green:#5b8e2c;
    --green-dark:#467320;
    --green-light:#8cbf4a;
    --ink:#2e2e2e;
    --body:#555;
    --grey-panel:#e9e9e9;
    --line:#9bb87a;
    --white:#fff;
  }
  *{box-sizing:border-box;margin:0;padding:0}
  html,body{width:1200px;height:2560px;overflow:hidden}
  body{background:var(--board);font-family:"Open Sans",Arial,sans-serif;color:var(--ink);position:relative}
  .board-title{position:absolute;top:56px;left:0;width:1200px;text-align:center;font-family:"Montserrat",Arial,sans-serif;font-weight:600;font-size:30px;color:var(--navy);letter-spacing:1px}
  .page{position:absolute;width:519px;height:734px;background:var(--white);overflow:hidden;box-shadow:0 14px 14px -8px rgba(0,0,0,.35)}
  .page-label{position:absolute;width:519px;text-align:center;font-family:"Montserrat",Arial,sans-serif;font-weight:500;font-size:23px;color:var(--ink);letter-spacing:.5px}

  .brand{display:flex;align-items:center;gap:6px;font-family:"Montserrat",Arial,sans-serif;font-weight:700;color:var(--ink)}
  .brand-mark{width:10px;height:10px;background:var(--green)}
  .page-header .brand{position:absolute;left:24px;top:28px;font-size:20px}
  .page-header .rule{position:absolute;left:140px;right:24px;top:40px;height:2px;background:var(--line)}

  .page-footer{position:absolute;left:24px;right:24px;bottom:28px;border-top:2px solid var(--line);padding-top:8px;display:flex;justify-content:space-between;font-family:"Montserrat",Arial,sans-serif;font-weight:600;font-size:10px;color:var(--ink)}

  .section-heading{font-family:"Montserrat",Arial,sans-serif;font-weight:700;font-size:15px;color:var(--ink);letter-spacing:.3px}
  .heading-rule{width:70px;height:2px;background:var(--green);margin-top:7px}
  .body-text{font-size:8.6px;line-height:1.55;color:var(--body)}
  .body-text p+p{margin-top:10px}

  /* cover */
  .cover{left:41px;top:137px;background:var(--grey-panel)}
  .cover .green-panel{position:absolute;left:255px;top:0;right:0;bottom:0;background:var(--green)}
  .cover .brand{position:absolute;left:36px;top:36px;font-size:34px}
  .cover .brand .brand-mark{width:14px;height:14px}
  .cover-titles{position:absolute;left:309px;top:34px;width:190px;color:var(--white);font-family:"Roboto Condensed","Arial Narrow",sans-serif;white-space:nowrap}
  .cover-titles .small{font-size:15px;font-weight:400}
  .cover-titles .mid{font-size:22px;font-weight:700;margin-top:3px;line-height:1.1}
  .cover-titles .big{font-size:28px;font-weight:700;line-height:1.1}
  .cover-titles .small.last{margin-top:2px}
  .cover-graphic{position:absolute;left:0;top:0}
  .cover-url{position:absolute;right:28px;bottom:36px;color:var(--white);font-family:"Montserrat",Arial,sans-serif;font-weight:700;font-size:14px;letter-spacing:.3px}

  /* contents */
  .contents{left:640px;top:137px}
  .toc{position:absolute;left:50px;top:135px;width:420px}
  .toc .section-heading{font-size:15px;margin-bottom:40px}
  .toc-row{display:flex;font-size:10px;color:var(--body);height:25.2px}
  .toc-row .entry{width:217px}
  .toc-row .dots{width:156px;letter-spacing:1px;color:#888}
  .toc-row .num{width:30px;text-align:right}

  /* feature page */
  .feature{left:41px;top:947px;background:radial-gradient(ellipse at 50% 40%,#66992f 0%,var(--green) 55%,var(--green-dark) 100%)}
  .feature-badge{position:absolute;left:0;right:0;top:110px;display:flex;justify-content:center;align-items:center;gap:10px;font-family:"Montserrat",Arial,sans-serif;font-weight:800;font-size:36px;color:var(--white);letter-spacing:1px}
  .feature-badge .dot{width:22px;height:22px;border-radius:50%;background:var(--white)}
  .feature-copy{position:absolute;left:51px;top:280px;width:420px;color:var(--white)}
  .feature-copy .section-heading{color:var(--white)}
  .feature-copy .heading-rule{width:420px;height:2px;background:var(--white);margin:8px 0 18px}
  .feature-copy .body-text{color:#eef5e6}
  .staff-photo{position:absolute;border-radius:14px 14px 0 0}
  .staff-photo.one{left:50px;top:482px;width:140px;height:252px;background:linear-gradient(160deg,#e7ddd2 0%,#8a7fa0 55%,#3b3b45 100%)}
  .staff-photo.two{left:300px;top:472px;width:110px;height:262px;background:linear-gradient(160deg,#e9ddcf 0%,#c9c7c0 50%,#c7442c 100%)}
  .staff-name{position:absolute;color:var(--white);text-align:center;font-family:"Montserrat",Arial,sans-serif}
  .staff-name b{display:block;font-size:9px;font-weight:600}
  .staff-name span{display:block;font-size:7px;line-height:1.3}
  .staff-name.one{left:198px;top:502px;width:80px}
  .staff-name.two{left:416px;top:496px;width:64px}

  /* page 4 */
  .insight{left:640px;top:947px}
  .insight .hero-photo{position:absolute;left:48px;top:82px;width:418px;height:285px;background:linear-gradient(135deg,#cfd6dc 0%,#eef1f3 45%,#8f9aa3 100%)}
  .insight .copy{position:absolute;left:48px;top:414px;width:438px}
  .insight .lead{margin:16px 28px 18px;text-align:center;font-size:8.6px;line-height:1.6;font-weight:700;color:var(--green)}

  /* page 5 */
  .article{left:41px;top:1755px}
  .article .copy{position:absolute;left:50px;top:118px;width:420px}
  .article .copy .heading-rule{margin-bottom:16px}
  .split{display:flex;gap:14px;margin:16px 0}
  .split .body-text{width:204px;text-align:justify}
  .split .side-photo{width:202px;height:150px;background:linear-gradient(135deg,#cfd6dc 0%,#eef1f3 45%,#8f9aa3 100%)}
  .pull-quote{position:absolute;left:50px;top:517px;width:418px;height:108px;border:2px solid var(--line);display:flex;align-items:center;justify-content:center;padding:0 36px;text-align:center}
  .pull-quote .mark{position:absolute;top:-26px;left:50%;transform:translateX(-50%);background:var(--white);padding:0 10px;font-family:"Montserrat",Arial,sans-serif;font-weight:800;font-size:52px;line-height:1;color:var(--green)}

  .closing-brand{position:absolute;left:671px;top:2080px;font-size:68px;gap:14px}
  .closing-brand .brand-mark{width:26px;height:26px}
</style>
</head>
<body>

<h1 class="board-title">WORD TEMPLATE</h1>

<!-- Cover -->
<section class="page cover">
  <div class="green-panel"></div>
  <svg class="cover-graphic" width="519" height="734" viewBox="0 0 519 734">
    <defs>
      <linearGradient id="coverArt" x1="0" y1="0" x2="1" y2="1">
        <stop offset="0" stop-color="#f3f1e4"/>
        <stop offset="0.5" stop-color="#ffffff"/>
        <stop offset="1" stop-color="#d9e8c4"/>
      </linearGradient>
    </defs>
    <circle cx="258" cy="360" r="214" fill="none" stroke="var(--green-dark)" stroke-width="16"/>
    <circle cx="258" cy="360" r="198" fill="url(#coverArt)" role="img" aria-label="Team values poster collage"/>
    <rect x="249" y="0" width="10" height="734" fill="#fff"/>
    <rect x="0" y="356" width="519" height="10" fill="#fff"/>
  </svg>
  <div class="brand"><span class="brand-mark"></span>Brovexa</div>
  <div class="cover-titles">
    <div class="small">Lorem Ipsum Goes Here</div>
    <div class="mid">LOREM IPSUM TEXT</div>
    <div class="big">LOREM IPSUM</div>
    <div class="small last">Lorem Ipsum Goes Here</div>
  </div>
  <div class="cover-url">www.brovexa.com.au</div>
</section>
<div class="page-label" style="left:41px;top:888px">COVER PAGE</div>

<!-- Contents -->
<section class="page contents">
  <header class="page-header"><div class="brand"><span class="brand-mark"></span>Brovexa</div><div class="rule"></div></header>
  <div class="toc">
    <h2 class="section-heading">TABLE OF CONTENTS</h2>
    <div class="toc-row"><span class="entry">Lorem Ipsum is simply dummy</span><span class="dots">- - - - - - - - - - - - - - -</span><span class="num">02</span></div>
    <div class="toc-row"><span class="entry">Lorem Ipsum is simply dummy</span><span class="dots">- - - - - - - - - - - - - - -</span><span class="num">03</span></div>
    <div class="toc-row"><span class="entry">Lorem Ipsum is simply dummy</span><span class="dots">- - - - - - - - - - - - - - -</span><span class="num">04</span></div>
    <div class="toc-row"><span class="entry">Lorem Ipsum is simply dummy</span><span class="dots">- - - - - - - - - - - - - - -</span><span class="num">05</span></div>
    <div class="toc-row"><span class="entry">Lorem Ipsum is simply dummy</span><span class="dots">- - - - - - - - - - - - - - -</span><span class="num">06</span></div>
    <div class="toc-row"><span class="entry">Lorem Ipsum is simply dummy</span><span class="dots">- - - - - - - - - - - - - - -</span><span class="num">07</span></div>
    <div class="toc-row"><span class="entry">Lorem Ipsum is simply dummy</span><span class="dots">- - - - - - - - - - - - - - -</span><span class="num">08</span></div>
    <div class="toc-row"><span class="entry">Lorem Ipsum is simply dummy</span><span class="dots">- - - - - - - - - - - - - - -</span><span class="num">09</span></div>
    <div class="toc-row"><span class="entry">Lorem Ipsum is simply dummy</span><span class="dots">- - - - - - - - - - - - - - -</span><span class="num">10</span></div>
  </div>
  <footer class="page-footer"><span>www.brovexa.com.au</span><span>2</span><span>support@brovexa.com.au</span></footer>
</section>
<div class="page-label" style="left:640px;top:888px">PAGE - 02</div>

<!-- Feature page -->
<section class="page feature">
  <div class="feature-badge"><span class="dot"></span>KELVORAN</div>
  <div class="feature-copy">
    <h2 class="section-heading">LOREM IPSUM DOLAR SIT</h2>
    <div class="heading-rule"></div>
    <div class="body-text">
      <p>Lorem Ipsum is simply dummy text of the printing and typesetting industry. Lorem Ipsum has been the industry's standard dummy text ever since the 1500s, when an unknown printer took a galley of type and scrambled it to make a type specimen book. It has survived not only five centuries, but also the leap into electronic typesetting, remaining essentially unchanged.</p>
      <p>Lorem Ipsum is simply dummy text of the printing and typesetting industry. Lorem Ipsum has been the industry's standard dummy text ever since the 1500s, when an unknown printer took a galley of type and scrambled it to make a type specimen book. It has survived not only five centuries, but also the leap into electronic typesetting, remaining essentially unchanged.</p>
    </div>
  </div>
  <div class="staff-photo one" role="img" aria-label="Support engineer holding a laptop"></div>
  <div class="staff-photo two" role="img" aria-label="Senior system engineer holding a book"></div>
  <div class="staff-name one"><b>MATEO</b><span>Support Engineer</span></div>
  <div class="staff-name two"><b>CALLUM</b><span>Senior System Engineer</span></div>
</section>
<div class="page-label" style="left:41px;top:1697px">PAGE - 03</div>

<!-- Page 4 -->
<section class="page insight">
  <header class="page-header"><div class="brand"><span class="brand-mark"></span>Brovexa</div><div class="rule"></div></header>
  <div class="hero-photo" role="img" aria-label="Hand with stylus pointing at analytics charts on a tablet"></div>
  <div class="copy">
    <h2 class="section-heading">LOREM IPSUM DOLAR SIT</h2>
    <div class="heading-rule"></div>
    <p class="lead">Lorem Ipsum is simply dummy text of the printing and typesetting industry. Lorem Ipsum has been the industry's standard dummy text ever since the 1500s, when an unknown printer took a galley of type and scrambled it to make a type specimen book.</p>
    <div class="body-text">
      <p>Lorem Ipsum is simply dummy text of the printing and typesetting industry. Lorem Ipsum has been the industry's standard dummy text ever since the 1500s, when an unknown printer took a galley of type and scrambled it to make a type specimen book. It has.</p>
      <p>Lorem Ipsum is simply dummy text of the printing and typesetting industry. Lorem Ipsum has been the industry's standard dummy text ever since the 1500s, when an unknown printer took a galley of type and scrambled it to make a type specimen book. It has.</p>
    </div>
  </div>
  <footer class="page-footer"><span>www.brovexa.com.au</span><span>4</span><span>support@brovexa.com.au</span></footer>
</section>
<div class="page-label" style="left:640px;top:1697px">PAGE - 04</div>

<!-- Page 5 -->
<section class="page article">
  <header class="page-header"><div class="brand"><span class="brand-mark"></span>Brovexa</div><div class="rule"></div></header>
  <div class="copy">
    <h2 class="section-heading">LOREM IPSUM DOLAR SIT</h2>
    <div class="heading-rule"></div>
    <p class="body-text">Lorem Ipsum is simply dummy text of the printing and typesetting industry. Lorem Ipsum has been the industry's standard dummy text ever since the 1500s, when an unknown printer took a galley of type and scrambled it to make a type specimen book. It has survived not only five centuries, but also the leap into electronic typesetting, remaining essentially unchanged.</p>
    <div class="split">
      <p class="body-text">Lorem Ipsum is simply dummy text of the printing and typesetting industry. Lorem Ipsum has been the industry's standard dummy text ever since the 1500s, when an unknown printer took a galley of type and scrambled it to make a type specimen book. It has survived not only five centuries, but also the typesetting, remaining unchanged. It was popularised in the 1960s.</p>
      <div class="side-photo" role="img" aria-label="Tablet showing analytics charts"></div>
    </div>
    <p class="body-text">Lorem Ipsum is simply dummy text of the printing and typesetting industry. Lorem Ipsum has been the industry's standard dummy text ever since the 1500s, when an unknown printer took a galley of type and scrambled it to make a type specimen book. It has survived not only five centuries, but also the leap into electronic typesetting, remaining essentially unchanged.</p>
  </div>
  <blockquote class="pull-quote">
    <span class="mark">&ldquo;</span>
    <p class="body-text">Lorem Ipsum is simply dummy text of the printing and typesetting industry. Lorem Ipsum has been the industry's standard dummy text ever since the 1500s, when an unknown printer took a galley of type and scrambled it to make a type specimen book. It has survived not only five centuries.</p>
  </blockquote>
  <footer class="page-footer"><span>www.brovexa.com.au</span><span>5</span><span>support@brovexa.com.au</span></footer>
</section>
<div class="page-label" style="left:41px;top:2505px">PAGE - 05</div>

<div class="brand closing-brand"><span class="brand-mark"></span>Brovexa</div>

</body>
</html>
```